Brisk Foundry PowerPoint Template

Project Title: Professional & Functional PowerPoint Template (.potx) – Brisk Foundry Rebrand

Project Overview:
Brisk Foundry has recently undergone a complete rebranding, including a new logo, website, and visual identity. We need a professional, high-end PowerPoint Template (.potx) that reflects our new look while being highly functional for everyday use.

We previously had a design created, but it was built incorrectly (static images, oversized file, no Master Slides). The goal of this project is to take our new aesthetic and build a "workable" template where layouts are controlled by Master Slides and text is easily editable.

Style & Brand Direction:
The template must be an extension of our new website: https://www.brisk-foundry.example/

Aesthetic: Modern, clean, high-tech, and "Industrial Tech."

Color Palette: Please pull the primary blues, greys, and accent colors directly from the website.

Imagery/Graphics: Use clean lines and subtle tech-inspired gradients. Avoid "clutter."

Tone: Innovative, precise, and professional.

Technical Requirements (Crucial)
Format: Must be delivered as a PowerPoint Template file (** .potx **).

Functionality: All layouts must be built using Slide Masters. Users should be able to click "New Slide" and choose from specific layouts.

Native Elements: Do NOT use full-page background images for text areas. Bullet points must use native PowerPoint list functionality (not individual text boxes).

File Size: The template must be optimized and lightweight.

Fonts: Use standard professional fonts or provide the specific web-safe equivalent used on our site (e.g., Montserrat, Open Sans, etc.).

Required Slide Layouts
Please include a minimum of 10–12 Master layouts, including:
*Title Slide (2-3 variations: Dark and Light)
*Agenda/Table of Contents
*Section Header/Divider Slides
*Standard Text/Bullet Slide
*Two-Column Text Slide
*Image + Text Layouts (Left/Right variations)
*Data/Chart Slide (Styled bar/pie charts that match the brand)
*Process/Timeline Slide (Infographic style)
*Section slide

Attachments Provided
Brand Assets (.zip): Contains our new logo in various formats.

Inspiration/Existing PPT: We have attached the previous design created by our web agency. Note: Use this for visual inspiration ONLY. Do not copy the file structure, as it is technically flawed.

Deliverables
Final .potx file.

All used icons or custom graphics in vector format (if applicable).

Instruction note on any specific fonts used.

Target Market(s)

Internal communication and external (investors, customers)

Industry/Entity Type

Semiconductor, Automotive

Requirements
Must have
• A potx file

```html
<!DOCTYPE html>
<html lang="en">
<head>
<meta charset="utf-8">
<title>Brisk Foundry – Slide Master Overview</title>
<link href="https://fonts.googleapis.com/css2?family=Inter:wght@400;500;700;800&display=swap" rel="stylesheet">
<style>
  :root{
    --navy:#0a1233;
    --ink:#111216;
    --blue:#2442d8;
    --blue-deep:#16268f;
    --grey:#c9ccd3;
    --grey-light:#eef0f4;
    --white:#ffffff;
    --text:#1c1d22;
    --muted:#6b6f7a;
  }
  *{box-sizing:border-box;margin:0;padding:0}
  html,body{width:686px;height:1200px;overflow:hidden;background:var(--white);font-family:"Inter",Arial,sans-serif;color:var(--text)}
  .sheet{position:relative;width:686px;height:1200px;display:grid;grid-template-columns:339px 339px;grid-template-rows:repeat(6,190px);column-gap:8px;row-gap:12px}
  .slide{position:relative;overflow:hidden;background:var(--white);border:1px solid #e2e4ea}
  .slide.dark{background:var(--navy);border-color:var(--navy)}
  .slide.blue{background:var(--blue);border-color:var(--blue)}
  .slide.black{background:var(--ink);border-color:var(--ink)}

  .brand{display:flex;align-items:center;gap:5px;font-weight:800;color:var(--white);font-size:15px;letter-spacing:.2px}
  .brand .mark{width:14px;height:14px;border:2px solid currentColor;border-radius:2px}
  .brand.blue-ink{color:var(--blue)}
  .headline{font-weight:800;color:var(--white);font-size:15px;line-height:1.15}
  .headline.dark-ink{color:var(--text)}

  /* title dark */
  .s1 .brand{position:absolute;left:14px;top:12px}
  .s1 .headline{position:absolute;left:14px;top:36px;width:300px}
  .s1 .panel{position:absolute;left:0;bottom:0;width:120px;height:82px;background:#121a3f;padding:10px}
  .s1 .panel p{font-size:5px;font-weight:700;color:var(--white);line-height:1.4;letter-spacing:.3px}
  .s1 .panel .btn{margin-top:28px;width:42px;height:8px;background:var(--white);font-size:3.5px;color:var(--navy);text-align:center;line-height:8px}
  .s1 .photo{position:absolute;right:0;bottom:0;width:219px;height:82px;background:linear-gradient(100deg,#1d3a2e 0%,#3a6b4a 35%,#1f4f7a 70%,#0e2244 100%);border-left:3px solid var(--blue)}

  /* title blue */
  .s2 .brand{position:absolute;left:14px;top:12px}
  .s2 .headline{position:absolute;left:14px;top:36px;width:310px;font-size:16px}
  .s2 .strip{position:absolute;left:0;right:0;bottom:0;height:46px;background:var(--navy);display:flex;justify-content:space-between;padding:10px 14px}
  .s2 .strip p{font-size:4px;color:#c9cfe8;line-height:1.5;width:80px}

  /* centered titles */
  .center{display:flex;flex-direction:column;align-items:center;justify-content:center;text-align:center;gap:6px}
  .center .brand{font-size:22px}
  .center .brand .mark{width:20px;height:20px;border-width:3px}
  .center .headline{width:230px}
  .center .sub{font-size:5px;color:var(--blue);font-weight:500}
  .s4 .sub{color:#cdd5ff}
  .s4{background:radial-gradient(circle at 70% 40%,#3556ea 0%,var(--blue) 45%,var(--blue-deep) 100%)}

  /* content slides */
  .title{position:absolute;left:12px;top:12px;font-size:13px;font-weight:800;color:var(--text)}
  .rail{position:absolute;top:0;right:0;width:22px;height:100%;border-left:1px solid #e2e4ea;display:flex;justify-content:center}
  .rail span{writing-mode:vertical-rl;font-weight:800;font-size:8px;color:var(--text);margin-top:10px}
  .rail i{position:absolute;bottom:6px;width:8px;height:8px;background:var(--blue)}
  .bullets{list-style:none}
  .bullets li{position:relative;padding-left:6px;font-size:4.6px;line-height:1.45;color:var(--muted);margin-bottom:5px}
  .bullets li::before{content:"";position:absolute;left:0;top:2.5px;width:2px;height:2px;background:var(--text)}

  .toc{position:absolute;left:12px;top:40px;width:295px;display:grid;grid-template-columns:1fr 1fr;column-gap:18px}
  .toc li{list-style:none;display:flex;align-items:center;font-size:5.5px;font-weight:700;height:20px;border-bottom:1px solid #eceef2}
  .toc b{color:var(--blue);width:16px}
  .toc em{margin-left:auto;width:7px;height:7px;background:var(--blue)}

  .s6 .bullets{position:absolute;left:12px;top:36px;width:290px}
  .s7 .cols{position:absolute;left:12px;top:40px;width:295px;display:grid;grid-template-columns:1fr 1fr;gap:14px}

  .s8 .photo{position:absolute;left:0;top:0;width:150px;height:100%;background:radial-gradient(circle at 40% 55%,#9fb0c8 0%,#4a5566 30%,#1a1e26 70%)}
  .s8 .title{left:160px;top:22px;font-size:14px;line-height:1.1}
  .s8 .bullets{position:absolute;left:160px;top:62px;width:150px}
  .s9 .title{font-size:14px;line-height:1.1}
  .s9 .bullets{position:absolute;left:12px;top:56px;width:150px}
  .s9 .photo{position:absolute;right:22px;top:0;width:150px;height:100%;background:linear-gradient(135deg,#262a30 0%,#4b5360 45%,#15181d 100%)}
  .s10 .title{left:175px}
  .s10 .bullets{position:absolute;left:175px;top:34px;width:135px}
  .s10 svg{position:absolute;left:14px;top:30px}
  .s11 .bullets{position:absolute;left:12px;top:36px;width:140px}
  .s11 svg{position:absolute;left:168px;top:30px}

  .s12 .brand{position:absolute;left:14px;top:50px;font-size:20px}
  .s12 .brand .mark{width:18px;height:18px}
  .s12 .headline{position:absolute;left:14px;top:82px;width:180px;font-size:13px}
  .s12 .drawing{position:absolute;right:0;top:0;width:120px;height:100%;background:linear-gradient(180deg,#1b1d22,#2a2d34)}
</style>
</head>
<body>
<main class="sheet">

  <section class="slide dark s1">
    <div class="brand"><span class="mark"></span>Brisk Foundry</div>
    <h1 class="headline">We collaborate to unlock new possibilities, not just deliver wafers.</h1>
    <div class="panel"><p>PRECISION WAFER<br>PRODUCTION<br>PARTNER</p><div class="btn">Learn more</div></div>
    <div class="photo" role="img" aria-label="Photo of glowing wafer production line"></div>
  </section>

  <section class="slide blue s2">
    <div class="brand"><span class="mark"></span>Brisk Foundry</div>
    <h1 class="headline">We collaborate to unlock new possibilities, not just deliver wafers.</h1>
    <div class="strip"><p>Presented by Name Surname, Chief Executive</p><p>Date<br>Month 00, 2025</p><p>Web<br>brisk-foundry.example</p></div>
  </section>

  <section class="slide s3 center">
    <div class="brand blue-ink"><span class="mark"></span>Brisk Foundry</div>
    <h1 class="headline dark-ink">We collaborate to unlock new possibilities, not just deliver wafers.</h1>
    <p class="sub">Subtitle here</p>
  </section>

  <section class="slide blue s4 center">
    <div class="brand"><span class="mark"></span>Brisk Foundry</div>
    <h1 class="headline">We collaborate to unlock new possibilities, not just deliver wafers.</h1>
    <p class="sub">Subtitle here</p>
  </section>

  <section class="slide s5">
    <h2 class="title">TABLE OF CONTENT</h2>
    <ul class="toc">
      <li><b>01.</b>COMPANY OVERVIEW<em></em></li><li><b>06.</b>BACKGROUND INFORMATION<em></em></li>
      <li><b>02.</b>PROBLEM AND SOLUTION<em></em></li><li><b>07.</b>RESEARCH METHODOLOGY<em></em></li>
      <li><b>03.</b>MARKET OPPORTUNITY<em></em></li><li><b>08.</b>LITERATURE REVIEW<em></em></li>
      <li><b>04.</b>OUR SERVICE AND PRODUCT<em></em></li><li><b>09.</b>RESULT AND DISCUSSION<em></em></li>
      <li><b>05.</b>MEET OUR TEAM<em></em></li><li><b>10.</b>RESULT AND DISCUSSION<em></em></li>
    </ul>
    <div class="rail"><span>Brisk Foundry</span><i></i></div>
  </section>

  <section class="slide s6">
    <h2 class="title">Standard Text/Bullet Slide</h2>
    <ul class="bullets">
      <li>Add a key point here with short supporting detail text for the audience today.</li>
      <li>Add a key point here with short supporting detail text for the audience today.</li>
      <li>Add a key point here with short supporting detail text for the audience today.</li>
      <li>Add a key point here with short supporting detail text for the audience today.</li>
      <li>Add a key point here with short supporting detail text for the audience today.</li>
      <li>Add a key point here with short supporting detail text for the audience today.</li>
      <li>Add a key point here with short supporting detail text for the audience today.</li>
      <li>Add a key point here with short supporting detail text for the audience today.</li>
    </ul>
    <div class="rail"><span>Brisk Foundry</span><i></i></div>
  </section>

  <section class="slide s7">
    <h2 class="title">Two-Column Text Slide</h2>
    <div class="cols">
      <ul class="bullets">
        <li>Add a key point here with short supporting detail text for the audience today.</li>
        <li>Add a key point here with short supporting detail text for the audience today.</li>
        <li>Add a key point here with short supporting detail text for the audience today.</li>
        <li>Add a key point here with short supporting detail text for the audience today.</li>
      </ul>
      <ul class="bullets">
        <li>Add a key point here with short supporting detail text for the audience today.</li>
        <li>Add a key point here with short supporting detail text for the audience today.</li>
        <li>Add a key point here with short supporting detail text for the audience today.</li>
        <li>Add a key point here with short supporting detail text for the audience today.</li>
      </ul>
    </div>
    <div class="rail"><span>Brisk Foundry</span><i></i></div>
  </section>

  <section class="slide s8">
    <div class="photo" role="img" aria-label="Close-up photo of a precision machining tool"></div>
    <h2 class="title">Left Image +<br>Text Layouts</h2>
    <ul class="bullets">
      <li>Add a key point here with short supporting detail text for the audience today.</li>
      <li>Add a key point here with short supporting detail text for the audience today.</li>
      <li>Add a key point here with short supporting detail text for the audience today.</li>
      <li>Add a key point here with short supporting detail text for the audience today.</li>
    </ul>
    <div class="rail"><span>Brisk Foundry</span><i></i></div>
  </section>

  <section class="slide s9">
    <h2 class="title">Left Image + Text<br>Layouts</h2>
    <ul class="bullets">
      <li>Add a key point here with short supporting detail text for the audience today.</li>
      <li>Add a key point here with short supporting detail text for the audience today.</li>
      <li>Add a key point here with short supporting detail text for the audience today.</li>
      <li>Add a key point here with short supporting detail text for the audience today.</li>
    </ul>
    <div class="photo" role="img" aria-label="Dark photo of industrial equipment"></div>
    <div class="rail"><span>Brisk Foundry</span><i></i></div>
  </section>

  <section class="slide s10">
    <svg width="150" height="140" viewBox="0 0 150 140" aria-label="Pie chart">
      <ellipse cx="72" cy="68" rx="62" ry="44" fill="#d9dce3"/>
      <path d="M72 64 L72 20 A62 44 0 1 1 14 80 Z" fill="#2442d8"/>
      <path d="M72 64 L14 80 A62 44 0 0 1 30 34 Z" fill="#111216"/>
      <rect x="20" y="124" width="5" height="5" fill="#2442d8"/><text x="28" y="128.5" font-size="5" fill="#555">Class 1</text>
      <rect x="60" y="124" width="5" height="5" fill="#111216"/><text x="68" y="128.5" font-size="5" fill="#555">Class 2</text>
      <rect x="100" y="124" width="5" height="5" fill="#c9ccd3"/><text x="108" y="128.5" font-size="5" fill="#555">Class 3</text>
    </svg>
    <h2 class="title">Data/Chart Slide</h2>
    <ul class="bullets">
      <li>Add a key point here with short supporting detail text for the audience today.</li>
      <li>Add a key point here with short supporting detail text for the audience today.</li>
      <li>Add a key point here with short supporting detail text for the audience today.</li>
      <li>Add a key point here with short supporting detail text for the audience today.</li>
      <li>Add a key point here with short supporting detail text for the audience today.</li>
    </ul>
    <div class="rail"><span>Brisk Foundry</span><i></i></div>
  </section>

  <section class="slide s11">
    <h2 class="title">Data/Chart Slide</h2>
    <ul class="bullets">
      <li>Add a key point here with short supporting detail text for the audience today.</li>
      <li>Add a key point here with short supporting detail text for the audience today.</li>
      <li>Add a key point here with short supporting detail text for the audience today.</li>
      <li>Add a key point here with short supporting detail text for the audience today.</li>
      <li>Add a key point here with short supporting detail text for the audience today.</li>
    </ul>
    <svg width="140" height="150" viewBox="0 0 140 150" aria-label="Bar chart">
      <g stroke="#e6e8ed" stroke-width=".6">
        <line x1="10" y1="20" x2="135" y2="20"/><line x1="10" y1="50" x2="135" y2="50"/>
        <line x1="10" y1="80" x2="135" y2="80"/><line x1="10" y1="110" x2="135" y2="110"/>
      </g>
      <line x1="10" y1="130" x2="135" y2="130" stroke="#999" stroke-width=".6"/>
      <rect x="22" y="20" width="12" height="110" fill="#2442d8"/>
      <rect x="36" y="84" width="12" height="46" fill="#111216"/>
      <rect x="62" y="104" width="12" height="26" fill="#2442d8"/>
      <rect x="76" y="70" width="12" height="60" fill="#111216"/>
      <rect x="102" y="114" width="12" height="16" fill="#c9ccd3"/>
      <rect x="116" y="108" width="12" height="22" fill="#c9ccd3"/>
      <rect x="30" y="140" width="4" height="4" fill="#2442d8"/><text x="36" y="144" font-size="5" fill="#555">Class 1</text>
      <rect x="62" y="140" width="4" height="4" fill="#111216"/><text x="68" y="144" font-size="5" fill="#555">Class 2</text>
      <rect x="94" y="140" width="4" height="4" fill="#c9ccd3"/><text x="100" y="144" font-size="5" fill="#555">Class 3</text>
    </svg>
    <div class="rail"><span>Brisk Foundry</span><i></i></div>
  </section>

  <section class="slide black s12">
    <div class="brand"><span class="mark"></span>Brisk Foundry</div>
    <h1 class="headline">We collaborate to unlock new possibilities, not just deliver wafers.</h1>
    <div class="drawing" role="img" aria-label="Line drawing of wafer processing equipment"></div>
  </section>

</main>
</body>
</html>
```